KalVesta Website- Joomla Template

A website for a Plumber company. A one page design ( this is what i mean http://pallowdesign.example/en/#graph)
The website should be a template for Joomla, i will do the website in 3 languages
I want it to be elegant but not so that it looks like a consulting company.
My customers are private customers, my products are :
Main focus is on Fixing 24/7
then renovate bathrooms
replace heating systems
and Maintenance
I need 12 slides:
Who we are
News
Service
Maintenance
Renewable Energy
Sanitary
Heating
Ventilation
Partners
Useful Links
Contact us
of course a Facebook, twitter and G+ icon
try to make an innovative nice menu

```html
<!DOCTYPE html>
<html lang="en">
<head>
<meta charset="utf-8">
<title>KalVesta – Plumbing, Heating &amp; Renovation</title>
<link rel="stylesheet" href="https://fonts.googleapis.com/css2?family=Noto+Serif:wght@400;700&family=Open+Sans:wght@400;600&display=swap">
<style>
:root{
  --blue:#1d4f86;
  --ink:#2f2f2f;
  --text:#3a3a3a;
  --muted:#8a8a8a;
  --line:#dcdcdc;
  --panel:#f3f3f3;
  --band:#ececec;
  --green:#4cbf5f;
  --red:#d9362b;
  --white:#ffffff;
}
*{box-sizing:border-box;margin:0;padding:0}
html,body{width:1200px;height:3561px;overflow:hidden;background:var(--white)}
body{font-family:"Noto Serif",Georgia,serif;color:var(--text)}
.section-title{font-family:"Noto Serif",Georgia,serif;font-weight:400;text-align:center;font-size:38px;letter-spacing:1px;color:var(--ink)}
.section-title.is-blue{color:var(--blue)}
.lead{font-size:12.5px;line-height:16px;text-align:center;color:var(--text)}

/* hero */
.hero{position:relative;height:591px;background:linear-gradient(180deg,#7d6a52 0%,#c7a67a 30%,#d9bd92 60%,#b58e5e 100%)}
.hero-photo{position:absolute;inset:0}
.hero-band{position:absolute;left:0;right:0;top:175px;height:255px;background:rgba(255,255,255,.82)}
.hero-badge{position:absolute;left:566px;top:92px;width:68px;height:68px;border-radius:50%;border:3px solid rgba(255,255,255,.9)}
.brand{position:absolute;left:0;right:0;top:270px;display:flex;justify-content:center;align-items:center;gap:18px}
.brand-dot{width:40px;height:40px;border-radius:50%;background:var(--blue)}
.brand-name{font-size:58px;color:var(--ink);line-height:1}
.slider-dots{position:absolute;left:0;right:0;top:548px;text-align:center}
.slider-dots span{display:inline-block;width:9px;height:9px;border-radius:50%;background:rgba(255,255,255,.6);margin:0 4px}
.slider-dots span.is-active{background:#fff}

/* nav */
.main-nav{height:72px;background:var(--band);display:flex;justify-content:center;align-items:center;gap:46px;font-family:"Open Sans",Arial,sans-serif;font-size:11px;letter-spacing:.5px;color:#333}
.nav-brand{font-family:"Noto Serif",Georgia,serif;font-size:15px;letter-spacing:0;color:var(--blue)}
.caret{font-size:8px;margin-left:3px}

/* about */
.about{height:283px;padding-top:60px}
.about .lead{width:900px;margin:22px auto 0}
.about .lead+.lead{margin-top:6px}

/* news */
.news{position:relative;height:378px;background:linear-gradient(100deg,#c9c9c9 0%,#e9e9e9 35%,#f4f4f4 60%,#dedede 100%)}
.news-photo{position:absolute;inset:0}
.news .section-title{position:relative;padding-top:58px}
.news-list{position:relative;display:flex;justify-content:center;gap:20px;margin-top:8px}
.news-card{width:155px;height:219px;background:rgba(255,255,255,.85);text-align:center;padding:6px}
.news-thumb{height:65px;background:linear-gradient(180deg,#8ea0ae,#c9a47b)}
.news-card h3{font-size:13px;font-weight:700;margin:12px 0 6px;color:#222}
.news-card p{font-size:10px;line-height:13px;color:#444}
.btn-outline{display:inline-block;margin-top:14px;border:1px solid var(--green);color:var(--green);font-family:"Open Sans",Arial,sans-serif;font-size:8px;padding:6px 12px}

/* services */
.services{position:relative;height:676px}
.services .section-title{padding-top:42px}
.services .lead{width:880px;margin:12px auto 0}
.service-grid{position:absolute;left:141px;top:213px;display:grid;grid-template-columns:repeat(3,296px);column-gap:16px;row-gap:77px}
.service-card{position:relative;height:180px;background:var(--panel);text-align:center;padding:52px 22px 0}
.service-icon{position:absolute;left:50%;top:-46px;margin-left:-46px;width:92px;height:92px;border-radius:50%;background:#fff}
.service-card h3{font-size:19px;font-weight:400;color:#222;margin-bottom:8px}
.service-card p{font-size:12px;line-height:15px;color:#333}

/* partners */
.partners{position:relative;height:377px;background:linear-gradient(110deg,#d6d2cc 0%,#ece9e4 40%,#f2f0ec 70%,#d8d4ce 100%)}
.partners-photo{position:absolute;inset:0}
.partners .section-title{position:relative;padding-top:50px}
.partner-list{position:absolute;top:115px;left:146px;display:flex;gap:10px}
.partner-card{width:221px;height:219px;background:#fff;text-align:center;box-shadow:0 1px 3px rgba(0,0,0,.2)}
.partner-photo{height:142px;background:linear-gradient(180deg,#b9b2a6,#2f3b57)}
.partner-card h3{font-size:24px;font-weight:400;color:#333;margin-top:12px}
.partner-card span{display:block;font-family:"Open Sans",Arial,sans-serif;font-size:10px;color:var(--muted);letter-spacing:.5px;margin-top:4px}

/* links */
.links{height:239px;padding-top:30px}
.link-cols{display:flex;justify-content:center;gap:60px;margin-top:26px;font-size:12px;text-align:center}
.link-cols ul{list-style:none;width:240px}
.link-cols li{margin-bottom:14px}
.link-cols li.is-active{color:var(--green);text-decoration:underline}

/* contact */
.contact-head{height:103px;background:var(--band);padding-top:42px}
.map{height:339px;background:linear-gradient(180deg,#d4d4d4,#c2c2c2 50%,#cfcfcf)}
.contact-info{position:relative;height:57px;font-family:"Open Sans",Arial,sans-serif;font-size:19px;color:#666}
.contact-item{position:absolute;top:0;height:57px;display:flex;align-items:center;gap:8px;white-space:nowrap}
.contact-item svg{fill:#777}
.contact-form{height:303px;background:var(--band);position:relative}
.field{position:absolute;height:36px;background:#fff;border:1px solid #e2e2e2;font-family:"Open Sans",Arial,sans-serif;font-size:12px;color:#999;padding:10px 14px}
.captcha-code{position:absolute;left:297px;top:211px;font-family:"Open Sans",Arial,sans-serif;font-size:13px;color:var(--red)}
.btn-send{position:absolute;left:766px;top:216px;width:110px;height:27px;background:var(--green);color:#fff;font-family:"Open Sans",Arial,sans-serif;font-size:9px;text-align:center;line-height:27px}

/* footer */
.site-footer{height:143px;text-align:center;padding-top:38px}
.social{display:flex;justify-content:center;gap:12px}
.social span{width:30px;height:30px;border-radius:50%;background:#d2d2d2}
.social span.is-active{background:#2f8fd8}
.copyright{margin-top:22px;font-family:"Open Sans",Arial,sans-serif;font-size:9px;letter-spacing:1px;color:#aaa}
</style>
</head>
<body>

<header class="hero">
  <div class="hero-photo" role="img" aria-label="Photo of plumbing tools laid out on a wooden workbench"></div>
  <div class="hero-band"></div>
  <div class="hero-badge" role="img" aria-label="Round emergency service badge"></div>
  <div class="brand">
    <span class="brand-dot"></span>
    <span class="brand-name">KalVesta</span>
  </div>
  <div class="slider-dots"><span></span><span class="is-active"></span><span></span><span></span></div>
</header>

<nav class="main-nav">
  <span>WHO WE ARE</span>
  <span>NEWS</span>
  <span>OUR SERVICES<span class="caret">▼</span></span>
  <span class="nav-brand">KalVesta</span>
  <span>PARTNERS</span>
  <span>USEFUL LINKS</span>
  <span>CONTACT US</span>
</nav>

<section class="about">
  <h2 class="section-title is-blue">WHO WE ARE</h2>
  <p class="lead">Lorem ipsum dolor sit amet, consectetuer adipiscing elit, sed diam nonummy nibh euismod tincidunt ut laoreet dolore magna aliquam erat volutpat. Ut wisi enim ad minim veniam, quis nostrud exerci tation ullamcorper suscipit lobortis nisl ut aliquip ex ea commodo consequat. Duis autem vel eum iriure dolor in hendrerit in vulputate velit esse molestie consequat, vel illum dolore eu feugiat nulla facilisis at vero eros et accumsan et iusto odio dignissim qui blandit praesent luptatum zzril delenit augue duis dolore te feugait nulla facilisi.</p>
  <p class="lead">Illum dolore eu feugiat nulla facilisis at vero eros et accumsan et iusto odio dignissim qui blandit praesent luptatum zzril delenit augue duis dolore te feugait nulla facilisi.</p>
</section>

<section class="news">
  <div class="news-photo" role="img" aria-label="Faded photo of a plumber working on pipes"></div>
  <h2 class="section-title">NEWS</h2>
  <div class="news-list">
    <article class="news-card"><div class="news-thumb" role="img" aria-label="Photo of pipe fittings"></div><h3>Latest News</h3><p>Dignissim qui blandit praesent luptatum zzril delenit augue duis dolore te feugait nulla facilisi.</p><span class="btn-outline">READ MORE</span></article>
    <article class="news-card"><div class="news-thumb" role="img" aria-label="Photo of pipe fittings"></div><h3>Latest News</h3><p>Dignissim qui blandit praesent luptatum zzril delenit augue duis dolore te feugait nulla facilisi.</p><span class="btn-outline">READ MORE</span></article>
    <article class="news-card"><div class="news-thumb" role="img" aria-label="Photo of pipe fittings"></div><h3>Latest News</h3><p>Dignissim qui blandit praesent luptatum zzril delenit augue duis dolore te feugait nulla facilisi.</p><span class="btn-outline">READ MORE</span></article>
    <article class="news-card"><div class="news-thumb" role="img" aria-label="Photo of pipe fittings"></div><h3>Latest News</h3><p>Dignissim qui blandit praesent luptatum zzril delenit augue duis dolore te feugait nulla facilisi.</p><span class="btn-outline">READ MORE</span></article>
    <article class="news-card"><div class="news-thumb" role="img" aria-label="Photo of pipe fittings"></div><h3>Latest News</h3><p>Dignissim qui blandit praesent luptatum zzril delenit augue duis dolore te feugait nulla facilisi.</p><span class="btn-outline">READ MORE</span></article>
  </div>
</section>

<section class="services">
  <h2 class="section-title is-blue">OUR SERVICES</h2>
  <p class="lead">Illum dolore eu feugiat nulla facilisis at vero eros et accumsan et iusto odio dignissim qui blandit praesent luptatum zzril delenit augue duis dolore te feugait nulla facilisi.</p>
  <div class="service-grid">
    <article class="service-card">
      <svg class="service-icon" viewBox="0 0 92 92"><circle cx="46" cy="46" r="42" fill="#fff" stroke="#222" stroke-width="3"/><path d="M30 30 L62 62 M62 30 L30 62" stroke="#222" stroke-width="7" stroke-linecap="round"/></svg>
      <h3>Service Maintenance</h3><p>Lorem ipsum dolor sit amet, consectetuer adipiscing elit. Nam vel turpis. Duis sit amet lectus ac mauris porta viverra.</p>
    </article>
    <article class="service-card">
      <svg class="service-icon" viewBox="0 0 92 92"><circle cx="46" cy="46" r="42" fill="#fff" stroke="#222" stroke-width="3"/><path d="M24 40 H58 V52 M40 40 V30 M32 30 H48" stroke="#222" stroke-width="7" fill="none" stroke-linecap="round"/><circle cx="58" cy="64" r="3" fill="#222"/></svg>
      <h3>Sanitary</h3><p>Lorem ipsum dolor sit amet, consectetuer adipiscing elit. Nam vel turpis. Duis sit amet lectus ac mauris porta viverra.</p>
    </article>
    <article class="service-card">
      <svg class="service-icon" viewBox="0 0 92 92"><circle cx="46" cy="46" r="42" fill="#fff" stroke="#222" stroke-width="3"/><circle cx="46" cy="40" r="12" fill="none" stroke="#222" stroke-width="4"/><path d="M46 52 V70 M38 70 H54" stroke="#222" stroke-width="5"/></svg>
      <h3>Renewable Energy</h3><p>Lorem ipsum dolor sit amet, consectetuer adipiscing elit. Nam vel turpis. Duis sit amet lectus ac mauris porta viverra.</p>
    </article>
    <article class="service-card">
      <svg class="service-icon" viewBox="0 0 92 92"><circle cx="46" cy="46" r="42" fill="#fff" stroke="#222" stroke-width="3"/><path d="M32 28 V64 M42 28 V64 M52 28 V64 M62 28 V64 M28 36 H66 M28 56 H66" stroke="#222" stroke-width="5"/></svg>
      <h3>Heating</h3><p>Lorem ipsum dolor sit amet, consectetuer adipiscing elit. Nam vel turpis. Duis sit amet lectus ac mauris porta viverra.</p>
    </article>
    <article class="service-card">
      <svg class="service-icon" viewBox="0 0 92 92"><circle cx="46" cy="46" r="42" fill="#fff" stroke="#222" stroke-width="3"/><circle cx="46" cy="46" r="22" fill="none" stroke="#222" stroke-width="4"/><path d="M46 46 L46 26 M46 46 L65 52 M46 46 L34 62" stroke="#222" stroke-width="5" stroke-linecap="round"/></svg>
      <h3>Ventilation</h3><p>Lorem ipsum dolor sit amet, consectetuer adipiscing elit. Nam vel turpis. Duis sit amet lectus ac mauris porta viverra.</p>
    </article>
    <article class="service-card">
      <svg class="service-icon" viewBox="0 0 92 92"><circle cx="46" cy="46" r="42" fill="#fff" stroke="#222" stroke-width="3"/><path d="M46 22 V70 M25 34 L67 58 M25 58 L67 34" stroke="#222" stroke-width="5" stroke-linecap="round"/></svg>
      <h3>Air Conditioning</h3><p>Lorem ipsum dolor sit amet, consectetuer adipiscing elit. Nam vel turpis. Duis sit amet lectus ac mauris porta viverra.</p>
    </article>
  </div>
</section>

<section class="partners">
  <div class="partners-photo" role="img" aria-label="Faded photo of a workshop with measuring tools"></div>
  <h2 class="section-title">PARTNERS</h2>
  <div class="partner-list">
    <article class="partner-card"><div class="partner-photo" role="img" aria-label="Portrait photo of a partner in a hard hat"></div><h3>JOHN DOE</h3><span>MEDIA PARTNER</span></article>
    <article class="partner-card"><div class="partner-photo" role="img" aria-label="Portrait photo of a partner holding tools"></div><h3>JOHN DOE</h3><span>PARTNER</span></article>
    <article class="partner-card"><div class="partner-photo" role="img" aria-label="Portrait photo of a partner in a hard hat"></div><h3>JOHN DOE</h3><span>MEDIA PARTNER</span></article>
    <article class="partner-card"><div class="partner-photo" role="img" aria-label="Portrait photo of a partner holding tools"></div><h3>JOHN DOE</h3><span>MEDIA PARTNER</span></article>
  </div>
</section>

<section class="links">
  <h2 class="section-title">LINKS</h2>
  <div class="link-cols">
    <ul><li>Lorem Ipsum</li><li>Dolor Sit Amet,</li><li>Lectus Ac Mauris Porta Viverra.</li></ul>
    <ul><li>Lorem Ipsum</li><li>Dolor Sit Amet,</li><li class="is-active">Lectus Ac Mauris Porta Viverra.</li><li>Consectetuer Adipiscing Elit.</li></ul>
    <ul><li>Lorem Ipsum</li><li>Dolor Sit Amet,</li><li>Lectus Ac Mauris Porta Viverra.</li></ul>
  </div>
</section>

<section class="contact">
  <div class="contact-head"><h2 class="section-title">CONTACT US</h2></div>
  <div class="map" role="img" aria-label="Grey world map showing the company location"></div>
  <div class="contact-info">
    <div class="contact-item" style="left:176px"><svg width="12" height="16" viewBox="0 0 12 16"><path d="M6 0a6 6 0 0 0-6 6c0 4 6 10 6 10s6-6 6-10a6 6 0 0 0-6-6zm0 8.5A2.5 2.5 0 1 1 6 3.5a2.5 2.5 0 0 1 0 5z"/></svg>CITY, XYZ</div>
    <div class="contact-item" style="left:491px"><svg width="14" height="14" viewBox="0 0 14 14"><path d="M3 0l3 3-2 2c1 2 3 4 5 5l2-2 3 3-2 3C6 14 0 8 0 3z"/></svg>12 34 56 789</div>
    <div class="contact-item" style="left:817px"><svg width="18" height="13" viewBox="0 0 18 13"><path d="M0 0h18v13H0z"/><path d="M1 1l8 6 8-6" stroke="#fff" fill="none" stroke-width="1.4"/></svg>info@kalvesta.example</div>
  </div>
  <div class="contact-form">
    <div class="field" style="left:293px;top:50px;width:234px">Name</div>
    <div class="field" style="left:293px;top:101px;width:234px">Email</div>
    <div class="field" style="left:293px;top:155px;width:234px">Phone</div>
    <span class="captcha-code">9ba9e</span>
    <div class="field" style="left:370px;top:202px;width:157px">Insert Captcha</div>
    <div class="field" style="left:553px;top:50px;width:336px;height:139px">Message</div>
    <div class="btn-send">SEND MESSAGE</div>
  </div>
</section>

<footer class="site-footer">
  <div class="social"><span></span><span class="is-active"></span><span></span></div>
  <p class="copyright">COPYRIGHT © 2014 KALVESTA INC.</p>
</footer>

</body>
</html>
```